Clothing Brand E-Commerce Website Design

We would like you to provide an ecommerce design template in layered PSD for our clothing/fashion brand website called "TrelWick".
We want the site to have a simple but sleek design similar to the following sites:
http://www.pivorane.com/
http://corvatelle.com/
http://www.dulvenor.com/
We want it to look stunning and blow the example sites out of the water. For color scheme, please use your imagination and try to impress us with your creativity.
We like teal and beige pink, with teal dominant.
Teal #7AFFFF / #46C6C6
Beige/pink #FF7B7C / #C74646
We want you to develop the design for 3 pages:
1) Home Page
Samples:
http://www.pivorane.com/
http://corvatelle.com/
http://www.dulvenor.com/
2) Products List Page (e.g., lists all "Dresses" when category is selected)
http://www.pivorane.com/shop/casual-dresses
http://www.dulvenor.com/index.php?main_page=index&cPath=3
http://corvatelle.com/modest-dresses.html
http://www.quillmarsh.com/Product/Category.aspx?br=q47&category=dress_maxi
3) Product Detail Page (e.g., individual product page with "Add to Cart")
http://www.pivorane.com/shop/dresses/lumen-fern-dress
http://corvatelle.com/modest-dresses/modest-dress-tova.html
http://www.dulvenor.com/index.php?main_page=product_info&cPath=3&products_id=297
Industry/Entity Type
Fashion

```html
<!DOCTYPE html>
<html lang="en">
<head>
<meta charset="utf-8">
<title>TrelWick — Clothing/Fashion Brand</title>
<link href="https://fonts.googleapis.com/css2?family=Aldrich&family=Roboto:wght@300;400&family=Roboto+Condensed:wght@700&family=Tinos&display=swap" rel="stylesheet">
<style>
:root{
  --teal:#46c6c6;
  --teal-light:#7affff;
  --pink:#ff7b7c;
  --ink:#333;
  --muted:#777;
  --rule:#9a9a9a;
  --soft:#e3e3e3;
  --paper:#fff;
}
*{box-sizing:border-box;margin:0;padding:0}
html,body{width:923px;height:1200px;overflow:hidden;background:var(--paper)}
body{font-family:"Aldrich",sans-serif;color:var(--ink);position:relative}
.abs{position:absolute}
.rule{position:absolute;height:1px;background:var(--rule)}
.vrule{position:absolute;width:1px;background:var(--rule)}
.nav a{position:absolute;font-size:9.5px;letter-spacing:.4px;color:var(--ink);text-decoration:none;text-transform:uppercase;white-space:nowrap}
.join{left:155px;top:64px;font-family:"Roboto",sans-serif;font-weight:300;font-size:19px;color:var(--teal)}
.brand{left:335px;width:232px;top:68px;text-align:center;font-size:42px;color:#3a3a3a;letter-spacing:.5px;line-height:50px}
.tagline{left:353px;top:127px;width:194px;height:17px;background:var(--teal);color:#fff;font-size:9.5px;letter-spacing:2px;text-align:center;line-height:17px}
.search{left:607px;top:63px;width:216px;height:20px;border:1px solid #aaa;font-family:"Roboto",sans-serif;font-size:10px;color:#777;padding-left:24px;line-height:18px}
.search svg{position:absolute;left:8px;top:3px}
.nav .active{color:var(--pink)}
.hero{left:76px;top:188px;width:770px;height:342px;
  background:
    radial-gradient(ellipse 90px 170px at 290px 190px,#c9c6bd 0%,rgba(201,198,189,0) 100%),
    radial-gradient(ellipse 260px 70px at 560px 70px,#efefea 0%,rgba(239,239,234,0) 100%),
    radial-gradient(ellipse 300px 110px at 600px 290px,#3a3a38 0%,rgba(58,58,56,0) 100%),
    radial-gradient(ellipse 180px 120px at 60px 290px,#4e4a44 0%,rgba(78,74,68,0) 100%),
    linear-gradient(180deg,#e4e4df 0%,#b8b8b2 45%,#6d6d68 100%)}
.arrow{position:absolute;top:333px;width:22px;height:44px;background:#fff}
.arrow.left{left:76px;clip-path:polygon(0 0,100% 50%,0 100%)}
.arrow.right{left:824px;clip-path:polygon(100% 0,0 50%,100% 100%)}
.arrow svg{position:absolute;top:17px}
.section-title{left:78px;top:558px;font-size:18px;letter-spacing:1.2px;font-weight:normal}
.product{position:absolute;top:598px;width:157px}
.product .photo{width:157px;height:125px;border:1px solid #ccc}
.product .name{margin-top:22px;text-align:center;font-size:12px;letter-spacing:.8px}
.product .price{text-align:center;font-size:12px;letter-spacing:.8px;margin-top:2px}
.btn{margin:6px 0 0 20px;width:111px;height:21px;background:var(--soft);font-size:9.5px;letter-spacing:.3px;display:flex;align-items:center;justify-content:center;gap:10px;color:#444}
.btn.hot{background:var(--teal-light);color:#111}
.shipping{left:77px;top:851px;width:369px;height:100px;border:2px solid var(--teal)}
.shipping .head{position:absolute;left:21px;top:13px;font-size:11px;line-height:16px;letter-spacing:.4px}
.shipping .amount{position:absolute;left:19px;top:45px;font-family:"Roboto Condensed",sans-serif;font-weight:700;font-size:32px;color:var(--teal)}
.shipping .note{position:absolute;left:188px;top:32px;font-family:"Courier New",monospace;font-size:10px;line-height:12px;color:#444}
.shipping svg{position:absolute;left:295px;top:12px}
.quote{left:476px;top:851px;width:214px;height:100px;border:1px solid #d8d8d8}
.quote::after{content:"";position:absolute;right:-6px;top:50px;width:10px;height:10px;background:#fff;border-right:1px solid #d8d8d8;border-top:1px solid #d8d8d8;transform:rotate(45deg)}
.quote h4{position:absolute;left:8px;top:14px;font-family:"Roboto",sans-serif;font-weight:400;font-size:11px}
.quote p{position:absolute;left:8px;top:38px;width:200px;font-family:"Roboto",sans-serif;font-weight:300;font-size:9.5px;line-height:12px;color:#666}
.avatar{left:717px;top:878px;width:44px;height:43px;background:radial-gradient(ellipse 14px 20px at 50% 40%,#c9b3a3,rgba(201,179,163,0)),linear-gradient(#e8e8e8,#555);border:1px solid #ccc}
.author{left:775px;top:884px;font-family:"Roboto",sans-serif;font-size:11px;color:#444}
.author small{display:block;font-size:9px;color:#888;margin-top:3px}
.serif-head{font-family:"Tinos",serif;font-size:13px;color:#444;letter-spacing:.3px;font-weight:normal}
.contact li{list-style:none;position:absolute;left:84px;display:flex;align-items:center;gap:6px;font-family:"Roboto",sans-serif;font-size:9px;color:#444}
.contact .mail{color:#c0307a}
.promo{left:274px;top:998px;width:368px;height:108px;
  background:
    radial-gradient(ellipse 70px 50px at 205px 35px,#f7e2b0,rgba(247,226,176,0)),
    linear-gradient(90deg,#fff 0%,#f08a5a 6%,#f4d63a 22%,#f2c89a 40%,#f0b8c8 55%,#f07a4a 70%,#c8303e 95%,#fff 100%)}
.newsletter p{font-family:"Roboto",sans-serif;font-size:9px;color:#444}
.field{left:655px;top:1058px;width:145px;height:16px;border:1px solid #999}
.subscribe{left:707px;top:1085px;width:72px;height:21px;background:var(--soft);font-family:"Roboto",sans-serif;font-size:9px;line-height:21px;text-align:center;color:#444}
.social span{position:absolute;top:1157px;width:22px;height:22px;background:#c8c8c8;border-radius:3px}
.footnav a{position:absolute;top:1162px;font-size:8.5px;letter-spacing:.6px;color:var(--ink);text-decoration:none}
</style>
</head>
<body>

<nav class="nav top-nav">
  <a style="left:78px;top:16px">New!</a>
  <a style="left:164px;top:16px">Tops</a>
  <a style="left:249px;top:16px">Bottoms</a>
  <a style="left:358px;top:16px">Dresses</a>
  <a style="left:463px;top:16px">Accessories</a>
  <a style="left:592px;top:16px">Clearance</a>
  <a style="left:712px;top:16px">Blog</a>
</nav>
<div class="rule" style="left:77px;top:36px;width:769px"></div>

<header>
  <div class="abs join">Join now</div>
  <div class="rule" style="left:77px;top:104px;width:258px"></div>
  <div class="vrule" style="left:335px;top:52px;height:103px"></div>
  <div class="vrule" style="left:567px;top:52px;height:103px"></div>
  <div class="abs brand">TrelWick</div>
  <div class="abs tagline">CLOTHING/FASHION BRAND</div>
  <div class="abs search">
    <svg width="11" height="11" viewBox="0 0 11 11"><circle cx="6.5" cy="4.5" r="3.6" fill="none" stroke="#999"/><line x1="3.8" y1="7.2" x2="1" y2="10" stroke="#999"/></svg>Search
  </div>
  <div class="rule" style="left:567px;top:101px;width:279px"></div>
  <nav class="nav">
    <a class="active" style="left:77px;top:131px">Home</a>
    <a style="left:141px;top:131px">All Products</a>
    <a style="left:255px;top:131px">Categories</a>
    <a style="left:609px;top:131px"><svg width="10" height="9" viewBox="0 0 10 9" style="vertical-align:-1px;margin-right:6px"><path d="M0 1h2l1.5 5h5l1-3.5H3" fill="#333"/><circle cx="4" cy="8" r="1" fill="#333"/><circle cx="8" cy="8" r="1" fill="#333"/></svg>My Cart</a>
    <a style="left:707px;top:131px">Checkout</a>
    <a style="left:789px;top:131px">Login</a>
  </nav>
</header>
<div class="rule" style="left:77px;top:171px;width:769px"></div>

<section>
  <div class="abs hero" role="img" aria-label="Hero photo: man in light blazer and sunglasses beside vintage cars"></div>
  <div class="arrow left"><svg width="10" height="10" style="left:2px" viewBox="0 0 10 10"><path d="M7 1L3 5l4 4" fill="none" stroke="#222" stroke-width="1.5"/></svg></div>
  <div class="arrow right"><svg width="10" height="10" style="left:10px" viewBox="0 0 10 10"><path d="M3 1l4 4-4 4" fill="none" stroke="#222" stroke-width="1.5"/></svg></div>
</section>
<div class="rule" style="left:76px;top:540px;width:770px"></div>

<section class="arrivals">
  <h2 class="abs section-title">NEW ARRIVALS</h2>
  <div class="product" style="left:77px">
    <div class="photo" role="img" aria-label="Woman in pale mint top" style="background:radial-gradient(ellipse 70px 50px at 50% 100%,#b9ddd2,rgba(185,221,210,0)),#f6f6f4"></div>
    <div class="name">DRAPA STYLING</div><div class="price">$100.00</div>
    <div class="btn hot"><svg width="10" height="9" viewBox="0 0 10 9"><path d="M0 1h2l1.5 5h5l1-3.5H3" fill="#222"/><circle cx="4" cy="8" r="1" fill="#222"/><circle cx="8" cy="8" r="1" fill="#222"/></svg>ADD TO CART</div>
  </div>
  <div class="product" style="left:281px">
    <div class="photo" role="img" aria-label="Man in red polo shirt" style="background:radial-gradient(ellipse 70px 55px at 50% 100%,#c65856,rgba(198,88,86,0)),#f6f6f4"></div>
    <div class="name">DRAPA STYLING</div><div class="price">$100.00</div>
    <div class="btn"><svg width="10" height="9" viewBox="0 0 10 9"><path d="M0 1h2l1.5 5h5l1-3.5H3" fill="#333"/><circle cx="4" cy="8" r="1" fill="#333"/><circle cx="8" cy="8" r="1" fill="#333"/></svg>ADD TO CART</div>
  </div>
  <div class="product" style="left:482px">
    <div class="photo" role="img" aria-label="Man in navy striped polo shirt" style="background:radial-gradient(ellipse 70px 55px at 50% 100%,#4f6298,rgba(79,98,152,0)),#f6f6f4"></div>
    <div class="name">DRAPA STYLING</div><div class="price">$100.00</div>
    <div class="btn"><svg width="10" height="9" viewBox="0 0 10 9"><path d="M0 1h2l1.5 5h5l1-3.5H3" fill="#333"/><circle cx="4" cy="8" r="1" fill="#333"/><circle cx="8" cy="8" r="1" fill="#333"/></svg>ADD TO CART</div>
  </div>
  <div class="product" style="left:688px">
    <div class="photo" role="img" aria-label="Woman in yellow lace top" style="background:radial-gradient(ellipse 70px 50px at 50% 100%,#e9d52a,rgba(233,213,42,0)),#f6f6f4"></div>
    <div class="name">DRAPA STYLING</div><div class="price">$100.00</div>
    <div class="btn"><svg width="10" height="9" viewBox="0 0 10 9"><path d="M0 1h2l1.5 5h5l1-3.5H3" fill="#333"/><circle cx="4" cy="8" r="1" fill="#333"/><circle cx="8" cy="8" r="1" fill="#333"/></svg>ADD TO CART</div>
  </div>
</section>

<section>
  <div class="abs shipping">
    <div class="head">FREE SHIPPING<br>ON ALL ORDER OVER</div>
    <div class="amount">$200</div>
    <div class="note">your own<br>banners<br>everywhere</div>
    <svg width="54" height="70" viewBox="0 0 54 70"><path d="M17 22V14a10 10 0 0 1 20 0v8" fill="none" stroke="#46c6c6" stroke-width="3"/><path d="M5 22h44l4 47H1z" fill="#46c6c6"/></svg>
  </div>
  <div class="abs quote">
    <h4>Mauris mattis molestie</h4>
    <p>Lorem ipsum dolor sit amet, consectetur adipiscing elit. Curabitur scelerisque ac sed commodo. Mauris quis arcu a neque...</p>
  </div>
  <div class="abs avatar" role="img" aria-label="Reviewer portrait"></div>
  <div class="abs author">Lorin Vask<small>14.04.2013</small></div>
</section>
<div class="rule" style="left:77px;top:973px;width:762px"></div>

<footer>
  <h3 class="abs serif-head" style="left:84px;top:998px">CONTACT INFO</h3>
  <ul class="contact">
    <li style="top:1021px"><svg width="20" height="20" viewBox="0 0 20 20"><circle cx="10" cy="10" r="9" fill="none" stroke="#444" stroke-width="1.6"/><path d="M10 15s-4-4-4-7a4 4 0 0 1 8 0c0 3-4 7-4 7z" fill="#444"/><circle cx="10" cy="8" r="1.4" fill="#fff"/></svg>48/6 Harbor St, New York City</li>
    <li style="top:1045px"><svg width="20" height="20" viewBox="0 0 20 20"><circle cx="10" cy="10" r="9" fill="none" stroke="#444" stroke-width="1.6"/><path d="M7 5l2 2-1 2c1 1.5 2 2.5 3 3l2-1 2 2-1.5 1.5C10 14 6 10 5.5 6.5z" fill="#444"/></svg>(+00)1572840-318</li>
    <li style="top:1069px" class="mail"><svg width="20" height="20" viewBox="0 0 20 20"><circle cx="10" cy="10" r="9" fill="none" stroke="#444" stroke-width="1.6"/><path d="M6 14l1-3 6-6 2 2-6 6z" fill="#444"/></svg>support@velnaro.com</li>
  </ul>
  <div class="abs promo" role="img" aria-label="Promo photo: surprised woman holding colourful shopping bags"></div>
  <div class="newsletter">
    <h3 class="abs serif-head" style="left:655px;top:998px">NEWSLETTER</h3>
    <p class="abs" style="left:655px;top:1022px">Stay informed on our latest news!</p>
    <p class="abs" style="left:655px;top:1043px">E-mail <span style="color:#c03030">*</span></p>
    <div class="abs field"></div>
    <div class="abs subscribe">SUBSCRIBE</div>
  </div>
  <div class="rule" style="left:77px;top:1141px;width:762px"></div>
  <div class="social">
    <span style="left:86px"></span><span style="left:117px"></span><span style="left:146px"></span><span style="left:176px"></span><span style="left:206px"></span>
  </div>
  <nav class="footnav">
    <a style="left:323px">NEW!</a>
    <a style="left:384px">TOPS</a>
    <a style="left:445px">BOTTOMS</a>
    <a style="left:525px">DRESSES</a>
    <a style="left:604px">ACCESSORIES</a>
    <a style="left:705px">CLEARANCE</a>
    <a style="left:799px">BLOG</a>
  </nav>
</footer>

</body>
</html>
```